Corvane Building Materials letterhead template

Simple but professional letterhead template for business communication.
LOGO/name in upper left, balanced by company contact info on right upper.
Subject description, date...
addressee, cc: and BC: if applicable editable info..

Need extra days to review

```html
<!DOCTYPE html>
<html lang="en">
<head>
<meta charset="UTF-8">
<title>Corvane Building Materials – Letterhead</title>
<link href="https://fonts.googleapis.com/css2?family=Lato:wght@400;700&family=Montserrat:wght@400&family=Allura&display=swap" rel="stylesheet">
<style>
  :root {
    --brand-blue: #285aa5;
    --rule-blue: #2b5aa3;
    --band-gray: #808080;
    --ink: #333333;
    --ink-dark: #222222;
    --paper: #ffffff;
    --paper-edge: #ececec;
    --backdrop: #dcd6cf;
  }
  * { margin: 0; padding: 0; box-sizing: border-box; }
  html, body {
    width: 1200px; height: 1200px; overflow: hidden;
    background: var(--backdrop);
  }
  .letterhead {
    position: absolute; left: 159px; top: 30px;
    width: 882px; height: 1140px;
    background: radial-gradient(ellipse at 50% 35%, var(--paper) 30%, var(--paper-edge) 100%);
    box-shadow: 0 6px 22px rgba(0,0,0,0.25);
    overflow: hidden;
    font-family: "Lato", sans-serif;
    color: var(--ink);
  }
  .brand {
    position: absolute; left: 69px; top: 76px;
    display: flex; align-items: center; gap: 12px;
  }
  .brand-dot {
    width: 18px; height: 18px; border-radius: 50%;
    background: var(--brand-blue);
  }
  .brand-name {
    font-family: "Lato", sans-serif; font-weight: 700;
    font-size: 24px; line-height: 28px;
    color: var(--ink-dark);
  }
  .contact {
    position: absolute; right: 69px; top: 52px;
    font-family: "Montserrat", sans-serif; font-size: 13.5px;
    line-height: 20.5px; color: var(--ink-dark);
    font-style: normal; white-space: nowrap;
  }
  .header-rule {
    position: absolute; left: 65px; top: 150px;
    width: 748px; height: 2.5px; background: var(--rule-blue);
  }
  .letter-body {
    position: absolute; left: 69px; top: 276px; width: 745px;
    font-size: 15.6px; line-height: 17.4px;
  }
  .date { margin-bottom: 21px; }
  .recipient, .company { margin-bottom: 19px; }
  .salutation {
    font-weight: 700; font-size: 19.5px; margin-bottom: 18px; color: var(--ink);
  }
  .paragraph { text-align: justify; margin-bottom: 17.5px; }
  .closing { margin-top: 38px; font-size: 15px; }
  .signature {
    font-family: "Allura", cursive; font-size: 42px;
    color: var(--ink-dark); margin-top: 22px; margin-left: 4px;
  }
  .footer-band-gray {
    position: absolute; left: 0; bottom: 86px;
    width: 100%; height: 14px; background: var(--band-gray);
  }
  .footer-band-blue {
    position: absolute; left: 0; bottom: 0;
    width: 100%; height: 80px; background: var(--brand-blue);
  }
</style>
</head>
<body>
  <main class="letterhead">
    <header>
      <div class="brand">
        <div class="brand-dot"></div>
        <div class="brand-name">Corvane Building Materials</div>
      </div>
      <address class="contact">
        CC :<br>
        BC :<br>
        P.O. BOX 42-07 NRT-15<br>
        Birchwood Ave 14, Fairhaven
      </address>
      <div class="header-rule"></div>
    </header>

    <section class="letter-body">
      <p class="date">Feb-03-2022</p>
      <p class="recipient">Mr, John Doe<br>President</p>
      <p class="company">Marlow Corporation<br>123 Street Name, Suite# 10<br>City, State, 120023</p>
      <p class="salutation">Dear Mr, John</p>
      <p class="paragraph">Lorem ipsum dolor sit amet, consectetur adipisicing elit, sed do eiusmod tempor incididunt ut labore et dolore magna aliqua. Ut enim ad minim veniam, quis nostrud exercitation ullamco laboris nisi ut aliquip ex ea commodo consequat. Duis aute irure dolor in reprehenderit in voluptate velit esse cillum dolore eu fugiat nulla pariatur.</p>
      <p class="paragraph">Lorem ipsum dolor sit amet, consectetur adipisicing elit, sed do eiusmod tempor incididunt ut labore et dolore magna aliqua. Ut enim ad minim veniam, quis nostrud exercitation ullamco laboris nisi ut aliquip ex ea commodo consequat. Duis aute irure dolor in reprehenderit in voluptate velit esse cillum dolore eu fugiat nulla pariatur.</p>
      <p class="paragraph">Lorem ipsum dolor sit amet, consectetur adipisicing elit, sed do eiusmod tempor incididunt ut labore et dolore magna aliqua. Ut enim ad minim veniam, quis nostrud exercitation ullamco laboris nisi ut aliquip ex ea commodo consequat.</p>
      <p class="paragraph">Excepteur sint occaecat cupidatat non proident, sunt in culpa qui officia deserunt mollit anim id est laborum. re et dolore magnam aliquam quaerat voluptatem.</p>
      <p class="closing">Regards</p>
      <p class="signature">Daniel Hart</p>
    </section>

    <footer>
      <div class="footer-band-gray"></div>
      <div class="footer-band-blue"></div>
    </footer>
  </main>
</body>
</html>
```